Business Card for boutique psychology business

Business card for boutique psychology practice in Melbourne. I want them to be relatively simply with the logo and backing colour taking up the front side. Then, text on the back, with my name; professional title (Clinical Psychologist); website - torvinpsychology.com.au; email: hello@torvinpsychology.com.au; insta: @torvin.psychology.emdr
Back should also have the words: Listen. Restore. Grow
Fonts used for logo are: Mikea Demo and Gotham Medium. Use something for back text that will compliment these.
Brand colours uploaded below. I'd like to see options in both olive and blush.

```html
<!DOCTYPE html>
<html lang="en">
<head>
<meta charset="utf-8">
<title>Torvin Psychology – Business Cards</title>
<link rel="stylesheet" href="https://fonts.googleapis.com/css2?family=Montserrat:wght@400;500;600&family=Crimson+Text:ital,wght@1,700&display=swap">
<style>
  :root {
    --blush: #e8c9bb;
    --olive: #3f4a2c;
    --olive-soft: #6b7350;
    --backdrop: #f1f1f1;
  }
  * { box-sizing: border-box; margin: 0; padding: 0; }
  html, body {
    width: 1200px;
    height: 1199px;
    overflow: hidden;
    background: var(--backdrop);
  }
  .canvas {
    position: relative;
    width: 1200px;
    height: 1199px;
  }
  .card {
    position: absolute;
    left: 304px;
    width: 595px;
    height: 340px;
    background: var(--blush);
    color: var(--olive);
    font-family: "Montserrat", sans-serif;
    overflow: hidden;
  }
  .card--front { top: 239px; }
  .card--back  { top: 621px; }

  .wordmark {
    position: absolute;
    font-family: "Montserrat", sans-serif;
    font-weight: 500;
    color: var(--olive);
    line-height: 1;
    letter-spacing: -0.01em;
  }
  .card--front .wordmark { left: 88px; top: 118px; font-size: 72px; }
  .card--back .wordmark  { left: 48px; top: 62px;  font-size: 52px; }

  .foliage {
    position: absolute;
    left: 402px;
    top: 0;
    width: 193px;
    height: 340px;
    background: linear-gradient(200deg, var(--olive-soft) 0%, #8f8f6c 45%, var(--blush) 100%);
    opacity: 0.85;
  }

  .holder {
    position: absolute;
    right: 41px;
    top: 38px;
    text-align: right;
  }
  .holder__name {
    font-weight: 600;
    font-size: 26px;
    line-height: 1.2;
  }
  .holder__title {
    font-weight: 400;
    font-size: 18px;
    margin-top: 6px;
    margin-right: 7px;
  }

  .contacts {
    position: absolute;
    right: 47px;
    top: 117px;
    list-style: none;
  }
  .contacts__item {
    display: flex;
    align-items: center;
    justify-content: flex-end;
    height: 42px;
    font-size: 18.5px;
    font-weight: 400;
  }
  .contacts__icon {
    width: 26px;
    height: 26px;
    margin-left: 8px;
    flex: none;
  }

  .tagline {
    position: absolute;
    left: 0;
    right: 0;
    top: 262px;
    text-align: center;
    font-family: "Crimson Text", serif;
    font-style: italic;
    font-weight: 700;
    font-size: 27px;
  }
</style>
</head>
<body>
<main class="canvas">

  <section class="card card--front" aria-label="Business card front">
    <div class="wordmark">torvin</div>
    <div class="foliage" role="img" aria-label="Olive leafy branch illustration along the right edge"></div>
  </section>

  <section class="card card--back" aria-label="Business card back">
    <div class="wordmark">torvin</div>

    <div class="holder">
      <p class="holder__name">Maren Holloway</p>
      <p class="holder__title">Clinical Psychologist</p>
    </div>

    <ul class="contacts">
      <li class="contacts__item">
        <span>torvinpsychology.com.au</span>
        <svg class="contacts__icon" viewBox="0 0 26 26" aria-hidden="true">
          <circle cx="13" cy="13" r="13" fill="var(--olive)"/>
          <g fill="none" stroke="var(--blush)" stroke-width="1.4">
            <circle cx="13" cy="13" r="7.5"/>
            <ellipse cx="13" cy="13" rx="3.2" ry="7.5"/>
            <line x1="5.5" y1="13" x2="20.5" y2="13"/>
            <line x1="7" y1="9" x2="19" y2="9"/>
            <line x1="7" y1="17" x2="19" y2="17"/>
          </g>
        </svg>
      </li>
      <li class="contacts__item">
        <span>hello@torvinpsychology.com.au</span>
        <svg class="contacts__icon" viewBox="0 0 26 26" aria-hidden="true">
          <circle cx="13" cy="13" r="13" fill="var(--olive)"/>
          <g fill="none" stroke="var(--blush)" stroke-width="1.4" stroke-linejoin="round">
            <rect x="6.5" y="8.5" width="13" height="9" rx="1"/>
            <polyline points="6.5,9 13,14 19.5,9"/>
          </g>
        </svg>
      </li>
      <li class="contacts__item">
        <span>@torvin.psychology.emdr</span>
        <svg class="contacts__icon" viewBox="0 0 26 26" aria-hidden="true">
          <circle cx="13" cy="13" r="13" fill="var(--olive)"/>
        </svg>
      </li>
    </ul>

    <p class="tagline">Listen. Restore. Grow</p>
  </section>

</main>
</body>
</html>
```